Inspirational Quote Poster for Employees

For this project, we need a simple yet high-impact poster template that will be customized for each of our employees with a personalized inspirational quote and color scheme. This template should allow us to quickly and easily customize the text and colors in the poster without a lot of effort.

The poster design should consist of:
- A stylized text area to contain the main text of the quote
- A separate text area to contain the source of quote
- A background that complements the color and style of the text

Text may use different typographic effects (such as color, stroke weight, italicization, font size changes, drop shadows) to draw attention to words in the quote; the source of the quote may be formatted the same as the main text of the quote, or may be formatted differently to distinguish it from the main quote.

The background may be simply a single color, subtle texture, gradients, halftone effects, or other color/texture effects may be used to complement the text.

Examples of the types of posters envisioned by this project:
- http://www.tackvale.com/corwinpmaddox/artquarry-job-1/

Sample quotes to use to build your poster - choose whichever one you want, but be certain that the poster design will handle both long and short quotes:
- "Happiness in intelligent people is the rarest thing I know" - Bertram Faulconer
- "Wanting to be someone else is a waste of the person you are." - Miles Tavenor
- "Experience is not what happens to you. It is what you do with what happens to you." - Cyril Pembrage
- "Simplicity is the ultimate in sophistication." - Ottaviano Restelli
- "You will get all you want in life if you help enough other people get what they want." - Hap Dunmore
- "Hell, there are no rules here — we're trying to accomplish something." - Walter Brisbane

Quote

• Final deliverable must be:
• - Formatted for an 18” x 24” poster (in portrait orientation)
• - Delivered in Adobe InDesign, Adobe Illustrator, or Extended PostScript format
• - Use CMYK color mode
• - Be print-ready at 300dpi resolution
• - Include any fonts used in the template

```html
<!DOCTYPE html>
<html lang="en">
<head>
<meta charset="utf-8">
<title>Quote Poster — Bertram Faulconer</title>
<link rel="stylesheet" href="https://fonts.googleapis.com/css2?family=Poppins:wght@400;600&family=Lobster+Two:ital,wght@1,700&display=swap">
<style>
  :root {
    --sky-light: #6cd6f9;
    --sky-mid: #3aa6df;
    --sky-deep: #0559ab;
    --ink: #ffffff;
  }
  html, body {
    margin: 0;
    padding: 0;
    width: 869px;
    height: 1200px;
    overflow: hidden;
  }
  .poster {
    display: block;
    width: 869px;
    height: 1200px;
  }
  .quote-caps {
    font-family: "Poppins", sans-serif;
    font-weight: 600;
    fill: var(--ink);
  }
  .quote-script {
    font-family: "Lobster Two", cursive;
    font-style: italic;
    font-weight: 700;
    fill: var(--ink);
  }
  .quote-source {
    font-family: "Poppins", sans-serif;
    font-weight: 400;
    fill: var(--ink);
    letter-spacing: 0.5px;
  }
</style>
</head>
<body>
<svg class="poster" viewBox="0 0 869 1200" xmlns="http://www.w3.org/2000/svg">
  <defs>
    <linearGradient id="backdrop" x1="0" y1="0.1" x2="1" y2="0">
      <stop offset="0" stop-color="var(--sky-light)"/>
      <stop offset="0.5" stop-color="var(--sky-mid)"/>
      <stop offset="1" stop-color="var(--sky-deep)"/>
    </linearGradient>
  </defs>
  <rect class="backdrop" width="869" height="1200" fill="url(#backdrop)"/>

  <g class="quote">
    <text class="quote-caps" x="48" y="370" font-size="136" textLength="772" lengthAdjust="spacingAndGlyphs">HAPPINESS</text>

    <text class="quote-script" x="46" y="478" font-size="100" textLength="80" lengthAdjust="spacingAndGlyphs">in</text>
    <text class="quote-caps" x="140" y="480" font-size="107" textLength="680" lengthAdjust="spacingAndGlyphs">INTELLIGENT</text>

    <text class="quote-caps" x="48" y="585" font-size="107" textLength="472" lengthAdjust="spacingAndGlyphs">PEOPLE</text>
    <text class="quote-script" x="560" y="585" font-size="100" textLength="258" lengthAdjust="spacingAndGlyphs">is the</text>

    <text class="quote-caps" x="48" y="720" font-size="157" textLength="772" lengthAdjust="spacingAndGlyphs">RAREST</text>

    <text class="quote-script" x="46" y="880" font-size="150" textLength="776" lengthAdjust="spacingAndGlyphs">thing I know</text>
  </g>

  <text class="quote-source" x="815" y="1170" font-size="30" text-anchor="end" textLength="330" lengthAdjust="spacingAndGlyphs">BERTRAM FAULCONER</text>
</svg>
</body>
</html>
```